Tour agency for FIT and groups need a business card design

We need a business card design for a tour agency company that is based in Perth called" BRISK NO", we aim to provide customise, unique and seamless travel arrangement for FIT and groups. We serve both high profile businessperson, government authorities, business partners, executives and investors. The name card should be more professional looking.
Updates

Project Deadline Extended Reason: Have some changes that needed to make, director will be back to office on Monday, sorry for the inconvenience cause. Added Saturday, May 6, 2017

Target Market(s)

High profile businessperson, government authorities, business partners, executives and investors.

Industry/Entity Type

Tourism

Contact Information for Business Card

Brisk NO
Level 1, 214 Marlowe Avenue, Dunreath NO, 6120
www.briskno.com.au

Font styles to use
Serif

Colors

Designer to choose colors to be used in the design.

Requirements
Must have
• My project must have a company logo
Nice to have
• a more professional and solid yet friendly name card design. We may want to include chinese name in the name card as well. Edge of the card can be filled with gold and we think that transparent name cards are interesting.

```html
<!DOCTYPE html>
<html lang="en">
<head>
<meta charset="utf-8">
<title>Brisk NO business card</title>
<link href="https://fonts.googleapis.com/css2?family=Lato:ital,wght@0,400;0,700;1,700&display=swap" rel="stylesheet">
<style>
  :root {
    --backdrop: #2e2e2e;
    --card: #ffffff;
    --brand-blue: #29a3dc;
    --ink: #1a1a1a;
    --ink-soft: #333333;
    --frame-grey: #d2d2d2;
  }
  html, body {
    margin: 0;
    width: 1200px;
    height: 1200px;
    overflow: hidden;
    background: var(--backdrop);
    font-family: "Lato", sans-serif;
  }
  .card {
    position: absolute;
    left: 258px;
    width: 684px;
    height: 410px;
    background: var(--card);
    box-shadow: 0 6px 16px rgba(0,0,0,0.45);
    overflow: hidden;
  }
  .card--front { top: 182px; }
  .card--back { top: 610px; }

  /* Front */
  .url-banner {
    position: absolute;
    left: 0;
    top: 82px;
    width: 323px;
    height: 58px;
    background: var(--brand-blue);
    clip-path: polygon(0 0, 100% 0, 92% 50%, 100% 100%, 0 100%);
  }
  .url-banner__text {
    position: absolute;
    left: 14px;
    top: 0;
    line-height: 58px;
    color: #fff;
    font-weight: 700;
    font-style: italic;
    font-size: 24px;
    letter-spacing: 0.2px;
  }
  .url-banner__dot {
    position: absolute;
    left: 338px;
    top: 99px;
    width: 24px;
    height: 24px;
    border-radius: 50%;
    background: var(--brand-blue);
  }
  .brand-name {
    position: absolute;
    color: var(--brand-blue);
    font-weight: 700;
    white-space: nowrap;
  }
  .card--front .brand-name {
    left: 330px;
    top: 218px;
    font-size: 60px;
  }

  /* Back */
  .plane-frame {
    position: absolute;
    inset: 0;
    background: var(--frame-grey);
  }
  .back-inner {
    position: absolute;
    left: 22px;
    top: 22px;
    right: 22px;
    bottom: 22px;
    background: var(--card);
  }
  .card--back .brand-name {
    right: 42px;
    top: 66px;
    font-size: 46px;
  }
  .holder-name {
    position: absolute;
    left: 38px;
    top: 148px;
    margin: 0;
    font-size: 31px;
    font-weight: 700;
    color: var(--ink);
  }
  .holder-role {
    position: absolute;
    left: 41px;
    top: 198px;
    font-size: 16px;
    color: var(--ink-soft);
  }
  .divider {
    position: absolute;
    left: 83px;
    top: 214px;
    width: 563px;
    height: 2px;
    background: var(--brand-blue);
  }
  .contact-list {
    position: absolute;
    left: 38px;
    top: 242px;
    margin: 0;
    padding: 0;
    list-style: none;
  }
  .contact-list li {
    display: flex;
    align-items: center;
    height: 33.5px;
    font-size: 16.5px;
    color: var(--ink-soft);
  }
  .contact-list svg {
    width: 16px;
    height: 16px;
    margin-right: 14px;
    fill: var(--brand-blue);
    flex: none;
  }
</style>
</head>
<body>

<section class="card card--front">
  <div class="url-banner"><span class="url-banner__text">www.briskno.com.au</span></div>
  <span class="url-banner__dot"></span>
  <span class="brand-name">Brisk NO</span>
</section>

<section class="card card--back">
  <div class="plane-frame" role="img" aria-label="Grey border pattern of small airplane motifs"></div>
  <div class="back-inner"></div>
  <span class="brand-name">Brisk NO</span>
  <h1 class="holder-name">Owen Hartley</h1>
  <span class="holder-role">Pilot</span>
  <span class="divider"></span>
  <ul class="contact-list">
    <li>
      <svg viewBox="0 0 16 16"><path d="M3.5 1.5l2.5 0 1 3.5-1.6 1.2a8 8 0 0 0 4.4 4.4l1.2-1.6 3.5 1v2.5c0 .8-.7 1.5-1.5 1.5C6.5 14 2 9.5 2 3c0-.8.7-1.5 1.5-1.5z"/></svg>
      00000-000000
    </li>
    <li>
      <svg viewBox="0 0 16 16"><path d="M1 3h14v10H1z M2 4.2v.3l6 4 6-4v-.3z" fill-rule="evenodd"/></svg>
      info@example.com
    </li>
    <li>
      <svg viewBox="0 0 16 16"><circle cx="8" cy="8" r="6.5" fill="none" stroke="#29a3dc" stroke-width="1.2"/><path d="M1.5 8h13M8 1.5c-3 3.5-3 9.5 0 13M8 1.5c3 3.5 3 9.5 0 13M2.5 5h11M2.5 11h11" fill="none" stroke="#29a3dc" stroke-width="1"/></svg>
      www.briskno.com.au
    </li>
    <li>
      <svg viewBox="0 0 16 16"><path d="M8 0.5a5 5 0 0 0-5 5c0 3.8 5 10 5 10s5-6.2 5-10a5 5 0 0 0-5-5zm0 7a2 2 0 1 1 0-4 2 2 0 0 1 0 4z"/></svg>
      Level 1, 214 Marlowe Avenue, Dunreath NO, 6120
    </li>
  </ul>
</section>

</body>
</html>
```